Site for a workout and Consulting enterprise

I need a professional responsive site for www.olvaru.hamburg. The website shoulderstand consist of a Landing and 4 other pages. - On page for the contact informations - on page for the about - on page for consulting services (technical) - on page for Training and workshop services (business and soft skills) I add some files so you can see my idea of the design.
Target Market(s)
IT and Management
Industry/Entity Type
Management Consulting
Coding
Coded - Design and coding required
Number of Pages Required
4 page
Requirements
Must have
- Use Pictures for Background, Sliders and Topics. Just have to placeholders for the design.

```html
<!DOCTYPE html>
<html lang="de">
<head>
<meta charset="utf-8">
<title>Olvaru – Training &amp; Consulting</title>
<link rel="stylesheet" href="https://fonts.googleapis.com/css2?family=Open+Sans:wght@400;600;700&display=swap">
<style>
  :root {
    --ink: #0b0b0b;
    --panel: rgba(8, 8, 8, 0.93);
    --white: #ffffff;
    --name: #eef8fc;
    --cyan: #22c3e6;
    --button-fill: rgba(110, 110, 110, 0.55);
    --sky: #8a8f93;
    --cloud: #3f474d;
    --hill: #45502c;
    --road: #6a6d6e;
    --road-dark: #3c3f40;
  }
  * { box-sizing: border-box; margin: 0; padding: 0; }
  html, body {
    width: 1200px;
    height: 640px;
    overflow: hidden;
    background: var(--ink);
    font-family: "Open Sans", Arial, sans-serif;
    color: var(--white);
  }
  .landing {
    position: relative;
    width: 1200px;
    height: 640px;
    overflow: hidden;
  }
  .hero-photo {
    position: absolute;
    inset: 0;
    background:
      radial-gradient(ellipse 420px 200px at 930px 110px, var(--sky) 0%, rgba(138,143,147,0) 100%),
      linear-gradient(180deg, var(--cloud) 0%, #4a5042 28%, var(--hill) 45%, #3b4226 62%, var(--road) 74%, var(--road-dark) 100%);
  }
  .brand-panel {
    position: absolute;
    left: 0;
    top: 0;
    width: 472px;
    height: 640px;
    background: var(--panel);
  }
  .brand {
    position: absolute;
    left: 0;
    width: 482px;
    top: 170px;
    text-align: center;
  }
  .brand-mark {
    display: block;
    width: 64px;
    height: 64px;
    margin: 0 auto 40px;
    border-radius: 50%;
    background: var(--cyan);
  }
  .brand-name {
    font-size: 43px;
    font-weight: 600;
    letter-spacing: 15px;
    line-height: 1;
    color: var(--name);
    padding-left: 15px;
  }
  .brand-tagline {
    margin-top: 14px;
    font-size: 16px;
    font-weight: 400;
  }
  .menu-toggle {
    position: absolute;
    left: 420px;
    top: 219px;
    width: 100px;
    height: 100px;
    border-radius: 50%;
    background: var(--ink);
  }
  .menu-toggle svg {
    position: absolute;
    left: 4px;
    top: 10px;
  }
  .copyright {
    position: absolute;
    left: 113px;
    top: 549px;
    font-size: 11.5px;
  }
  .footer-link {
    position: absolute;
    top: 535px;
    width: 245px;
    height: 47px;
    border: 2px solid var(--white);
    border-radius: 24px;
    background: var(--button-fill);
    font-size: 16px;
    font-weight: 700;
    line-height: 43px;
    text-align: center;
    color: var(--white);
    text-decoration: none;
  }
  .footer-link.impressum { left: 587px; }
  .footer-link.kontakt { left: 845px; }
  .version-tag {
    position: absolute;
    left: 1150px;
    top: 550px;
    font-size: 14px;
    font-weight: 700;
  }
</style>
</head>
<body>
<main class="landing">
  <div class="hero-photo" role="img" aria-label="Background photo: mountain road with START painted on the asphalt, green hillside and cloudy sky"></div>

  <section class="brand-panel">
    <div class="brand">
      <span class="brand-mark"></span>
      <div class="brand-name">OLVARU</div>
      <div class="brand-tagline">Training &amp; Consulting</div>
    </div>
    <div class="copyright">Copyrights © 2017, Olvaru. All Rights Reserved.</div>
  </section>

  <div class="menu-toggle" aria-label="Menü öffnen">
    <svg width="82" height="82" viewBox="0 0 82 82">
      <circle cx="41" cy="41" r="41" fill="var(--cyan)"/>
      <rect x="30" y="38.5" width="22" height="5" rx="1" fill="#fff"/>
      <rect x="38.5" y="30" width="5" height="22" rx="1" fill="#fff"/>
    </svg>
  </div>

  <a class="footer-link impressum" href="#">IMPRESSUM</a>
  <a class="footer-link kontakt" href="#">KONTAKT</a>
  <div class="version-tag">C17</div>
</main>
</body>
</html>
```